Northern Summit Builders & Affiliates Redesigning our Look

We need stationary (letterhead, envelopes, notepads, invoicing templates, etc) that all coordinate. We are an commerial and residential exteriors construction company that operates 3 companies which all run exclusively, however, the compliment one another well.

Northern Summit Builders (this company installs exteriors on jobsites both residential and commercial)
Northern Summit Roofing & Building Supply (this company sells exterior building materials to homeowners and builders.)
Northern Summit Dumpster Services (This company delivers roll away dumpster cans to homeowners and builders)

Just a note: When I say we do exterior work. We do roofing, siding, stone, windows/doors, gutters, and decks.

We are looking for stationary that includes all three and keeps with our patriotic theme

Info on our firm:
Address: 2718 Tamarind Rd, Elkton MI 48512
Phone: 231-555-0172
Website: www.northernsummit-example.us

Target Market(s)

Our companies target market is vast. We work in the B2B space as well as with homeowner (retail customers). We are in the home and commercial buiding construction field. We specialized in exteriors. (Roofing, Siding, Stone, Windows, Doors, Decks, Gutters)

Industry/Entity Type

Construction

Colors
ec1f27
ffffff
0555a3

Requirements
Must have
• Would like to have a clean professional look with a patriotic theme
Nice to have
• Red/White/Blue

```html
<!DOCTYPE html>
<html lang="en">
<head>
<meta charset="utf-8">
<title>Northern Summit Builders – Business Card</title>
<link rel="stylesheet" href="https://fonts.googleapis.com/css2?family=Open+Sans:wght@400;600;700&display=swap">
<style>
  :root {
    --page-bg: #e6e4e0;
    --card-bg: #ffffff;
    --ink: #222222;
    --ink-soft: #555555;
    --navy: #2b2f7e;
    --red: #ec1f27;
    --blue: #0555a3;
  }
  * { box-sizing: border-box; margin: 0; padding: 0; }
  html, body {
    width: 1200px;
    height: 950px;
    overflow: hidden;
    background: var(--page-bg);
    font-family: "Open Sans", Arial, sans-serif;
  }
  .canvas {
    width: 1200px;
    height: 950px;
    display: flex;
    align-items: center;
    justify-content: center;
  }
  .business-card {
    width: 1050px;
    height: 600px;
    background: var(--card-bg);
    border-radius: 34px;
    box-shadow: 0 14px 40px rgba(0,0,0,0.18);
    display: flex;
    flex-direction: column;
    align-items: center;
    justify-content: center;
    text-align: center;
  }
  .brand {
    display: flex;
    align-items: center;
    gap: 18px;
    margin-bottom: 34px;
  }
  .brand-mark {
    width: 46px;
    height: 46px;
    background: var(--red);
  }
  .brand-name {
    font-size: 62px;
    font-weight: 700;
    color: var(--ink);
    letter-spacing: -0.5px;
    line-height: 1;
  }
  .person-name {
    font-size: 40px;
    font-weight: 700;
    color: var(--navy);
    letter-spacing: 1px;
    line-height: 1.1;
  }
  .person-title {
    font-size: 27px;
    font-weight: 400;
    color: var(--red);
    margin-bottom: 40px;
  }
  .contact-line {
    font-size: 24px;
    color: var(--ink-soft);
    line-height: 1.5;
  }
  .contact-line .label {
    font-weight: 700;
    color: var(--navy);
  }
  .website {
    font-size: 25px;
    color: var(--navy);
    line-height: 1.6;
  }
</style>
</head>
<body>
  <main class="canvas">
    <section class="business-card">
      <div class="brand">
        <span class="brand-mark" aria-hidden="true"></span>
        <span class="brand-name">Northern Summit</span>
      </div>
      <h1 class="person-name">DANIEL REYES</h1>
      <p class="person-title">CEO/Founder</p>
      <p class="contact-line">2718 Tamarind Rd, Elkton MI 48512</p>
      <p class="contact-line"><span class="label">(P)</span> 231-555-0172 <span class="label">(E)</span> dreyes@northernsummit-example.us</p>
      <p class="website">www.northernsummit-example.us</p>
    </section>
  </main>
</body>
</html>
```